Namecard Designs+Logo for a High End Automobile Company

We need a new business card for our company called Velta Motorhof.

www.veltamotorhof.example.sg
Our new website will be up in 2.5 months time.

We sell used and brand new continental cars like Korvane, QTL, Dravell, Solbrini and etc. Currently we are operating from 2 offices in Singapore and United Kingdom.

We want a design which is serious. We are open to colours but try to keep it at a maximum of 3 colours.

We prefer something simple and minimal. We are open to 2 sides printing or even 2 sided namecards. Both UK and Singapore company offices address must be in; either side by side, front and back, or even 2 sided cards.

The logo can be a text logo, emblem, abstract, pictorial or combination.

We are printing with Pribo.com so please kindly follow the printing guideline.

http://uk.pribo.example/help/faq/templates-and-guidelines.html

Rich and Car Enthusiasts

Printing

Must have
• Our 2 offices; UK and Singapore.

Our slogan which is " The Automobile Specialist"
Should not have
• Not more than 3 colours

```html
<!DOCTYPE html>
<html lang="en">
<head>
<meta charset="utf-8">
<title>Velta Motorhof – Business Card</title>
<link rel="stylesheet" href="https://fonts.googleapis.com/css2?family=Arimo:wght@400;700&family=Tinos&display=swap">
<style>
  :root {
    --page: #e6e6e6;
    --card-black: #0b0b0b;
    --card-dark: #1c1c1c;
    --chrome-light: #d9d9d9;
    --chrome-mid: #8a8a8a;
    --chrome-dark: #3a3a3a;
    --text-white: #f4f4f4;
    --logo-silver: #c8c8c8;
  }
  * { margin: 0; padding: 0; box-sizing: border-box; }
  html, body {
    width: 1200px;
    height: 801px;
    overflow: hidden;
    background: var(--page);
  }
  .card {
    position: absolute;
    top: 240px;
    width: 540px;
    height: 320px;
    border-radius: 4px;
    overflow: hidden;
    background: var(--card-black);
    box-shadow: 0 2px 6px rgba(0,0,0,0.25);
  }
  .card--back { left: 40px; }
  .card--front { left: 620px; }

  /* back side */
  .headlight-art {
    position: absolute;
    left: 0; top: 0;
    width: 100%;
    height: 160px;
    background:
      radial-gradient(ellipse 120px 60px at 18% 55%, var(--card-dark) 60%, transparent 62%),
      radial-gradient(ellipse 120px 60px at 82% 55%, var(--card-dark) 60%, transparent 62%),
      linear-gradient(180deg, var(--chrome-light) 0%, var(--chrome-mid) 45%, var(--chrome-dark) 80%, var(--card-black) 100%);
    border-bottom-left-radius: 50% 30px;
    border-bottom-right-radius: 50% 30px;
  }
  .name-plate {
    position: absolute;
    left: 170px; top: 92px;
    width: 200px; height: 62px;
    border-radius: 22px;
    background: linear-gradient(180deg, #5a5a5a 0%, #2a2a2a 100%);
    border: 2px solid var(--chrome-light);
    text-align: center;
    color: var(--text-white);
  }
  .name-plate__name {
    font-family: "Tinos", serif;
    font-size: 27px;
    line-height: 1;
    margin-top: 9px;
  }
  .name-plate__title {
    font-family: "Arimo", sans-serif;
    font-size: 11px;
    margin-top: 5px;
  }
  .contact {
    position: absolute;
    left: 50px; top: 190px;
    width: 450px;
    font-family: "Arimo", sans-serif;
    font-size: 12px;
    line-height: 17px;
    color: var(--text-white);
  }
  .contact__row { display: flex; }
  .contact__label { width: 72px; flex-shrink: 0; }
  .contact__value { flex: 1; white-space: nowrap; }
  .contact__side { width: 150px; text-align: right; white-space: nowrap; }

  /* front side */
  .mesh-surface {
    position: absolute;
    inset: 0;
    background: radial-gradient(ellipse at 55% 35%, #2a2a2a 0%, #141414 55%, #050505 100%);
  }
  .brand-mark {
    position: absolute;
    left: 0; top: 100px;
    width: 100%;
    text-align: center;
    font-family: "Arimo", sans-serif;
    font-weight: 400;
    font-size: 56px;
    line-height: 1;
    color: var(--logo-silver);
  }
  .slogan {
    position: absolute;
    left: 0; top: 186px;
    width: 100%;
    text-align: center;
    font-family: "Arimo", sans-serif;
    font-weight: 700;
    font-size: 24px;
    color: var(--text-white);
  }
</style>
</head>
<body>
  <section class="card card--back">
    <div class="headlight-art" role="img" aria-label="Chrome headlight and grille artwork"></div>
    <div class="name-plate">
      <div class="name-plate__name">Your Name</div>
      <div class="name-plate__title">General manager</div>
    </div>
    <div class="contact">
      <div class="contact__row">
        <span class="contact__label">Adress:</span>
        <span class="contact__value">SG: 18 Kelvin Rd. Harbourview, Singapore</span>
      </div>
      <div class="contact__row">
        <span class="contact__label"></span>
        <span class="contact__value">UK: 4 Fenwick Lane, Ashbury, United Kingdom</span>
      </div>
      <div class="contact__row">
        <span class="contact__label">Email:</span>
        <span class="contact__value">info@veltamotorhof.example.sg</span>
        <span class="contact__side">(065) 555 0127</span>
      </div>
      <div class="contact__row">
        <span class="contact__label">Tel - Fax:</span>
        <span class="contact__value">555 0127</span>
        <span class="contact__side">Mobile: (065) 555 0128</span>
      </div>
      <div class="contact__row">
        <span class="contact__label"></span>
        <span class="contact__value">555 0127</span>
      </div>
    </div>
  </section>

  <section class="card card--front">
    <div class="mesh-surface" role="img" aria-label="Dark carbon mesh texture"></div>
    <div class="brand-mark">Velta Motorhof</div>
    <div class="slogan">The Automobile Specialist</div>
  </section>
</body>
</html>
```